Postcard Design for Brandvold Tree Farm LLC

We are a small family owned Christmas tree farm. We work with various groups on their fundraising programs selling wreaths and trees. Our goal is to expand our business, advertising with post cards.

Target Market(s)

Schools, Ridgeway Cadets, various non profit groups

Industry/Entity Type

Advertising

Requirements
Must have
• Front side-

Let us help you develop a successful holiday fundraiser for your group with fresh, fragrant Wisconsin wreaths shipped directly from our farm!

Picture of a real wreath with a red bow and 2 pinecone clusters at 4 o'clock and 8 o'clock.

Contact information -
Brandvold Tree Farm LLC
www.brandvoldtreefarm.example
318-406-7192

Backside -
We have 2 different type of wreath fundraising programs - mail order and direct distribution. You group can choose to do one or both. Wholesale Christmas trees are also available.

```html
<!DOCTYPE html>
<html lang="en">
<head>
<meta charset="utf-8">
<title>Brandvold Tree Farm – Wreath Fundraiser Postcard</title>
<link rel="stylesheet" href="https://fonts.googleapis.com/css2?family=Montserrat:wght@500;700;800&family=Libre+Baskerville&display=swap">
<style>
  :root {
    --bg: #b9b9b7;
    --wood-dark: #4a1e10;
    --wood-mid: #7a3420;
    --wood-light: #9b4a2c;
    --banner: #3f5f1c;
    --white: #ffffff;
    --paper: #f7f7f5;
    --line-green: #2f7a2a;
    --field-dark: #2e2e2e;
    --field-light: #cfcfcf;
  }
  * { box-sizing: border-box; margin: 0; padding: 0; }
  html, body { width: 1200px; height: 1000px; overflow: hidden; }
  body {
    background: var(--bg);
    font-family: "Montserrat", Arial, sans-serif;
    display: flex; flex-direction: column; align-items: center; justify-content: center;
    gap: 24px;
  }
  .postcard {
    position: relative;
    width: 690px; height: 465px;
    overflow: hidden;
    box-shadow: 0 6px 16px rgba(0,0,0,.25);
  }

  /* Front */
  .front__photo {
    position: absolute; inset: 0;
    background:
      radial-gradient(circle at 50% 36%, #1f4a1c 0 18%, transparent 18.5%),
      radial-gradient(circle at 50% 36%, #b0121a 0 6%, transparent 6.5%),
      repeating-linear-gradient(90deg, var(--wood-dark) 0 6px, var(--wood-mid) 6px 70px, var(--wood-light) 70px 110px, var(--wood-mid) 110px 170px);
  }
  .front__frame {
    position: absolute; inset: 14px;
    border: 4px solid var(--white);
    border-radius: 4px;
  }
  .front__banner {
    position: absolute; left: 0; top: 300px;
    width: 420px; padding: 14px 30px 14px 28px;
    background: var(--banner);
    clip-path: polygon(0 0, 100% 0, 96% 50%, 100% 100%, 0 100%);
    color: var(--white);
    font-weight: 800; font-size: 16px; line-height: 1.25;
    letter-spacing: .3px;
    text-align: justify;
  }
  .front__contact {
    position: absolute; right: 40px; top: 370px;
    color: var(--white);
    font-weight: 700; font-size: 10px; line-height: 1.45;
  }
  .front__contact .contact__phone { font-size: 11px; font-weight: 500; }

  /* Back */
  .back { background: var(--paper); display: flex; }
  .back__photo {
    position: relative;
    width: 300px; height: 100%;
    background: linear-gradient(180deg, var(--field-dark) 0%, #4a4a4a 45%, #6d6d6d 62%, var(--field-light) 78%, #e2e2e2 100%);
  }
  .back__message {
    position: absolute; top: 26px; left: 22px; right: 18px;
    color: var(--white);
    font-weight: 700; font-size: 14px; line-height: 1.3;
    text-align: justify;
  }
  .back__brand {
    position: absolute; left: 22px; bottom: 26px;
    color: var(--white);
    font-family: "Libre Baskerville", Georgia, serif;
    font-size: 17px; line-height: 1.2;
  }
  .back__address {
    position: relative; flex: 1;
    padding: 48px 40px 0 56px;
  }
  .stamp-box {
    position: absolute; top: 36px; right: 40px;
    width: 82px; height: 76px;
    border: 2px solid var(--line-green);
  }
  .address-lines { list-style: none; margin-top: 120px; }
  .address-lines li {
    height: 40px;
    border-bottom: 1.5px solid var(--line-green);
  }
</style>
</head>
<body>

  <section class="postcard front">
    <div class="front__photo" role="img" aria-label="Photo of a fresh evergreen wreath with a red bow and pinecone clusters hanging on a dark wooden front door"></div>
    <div class="front__frame"></div>
    <p class="front__banner">Let us help you develop a successful holiday fundraiser for your group with fresh, fragrant Wisconsin wreaths shipped directly from our farm!</p>
    <div class="front__contact">
      <p class="contact__name">Brandvold Tree Farm LLC</p>
      <p class="contact__web">www.brandvoldtreefarm.example</p>
      <p class="contact__phone">318-406-7192</p>
    </div>
  </section>

  <section class="postcard back">
    <div class="back__photo" role="img" aria-label="Black and white photo of rows of young Christmas trees in a snowy field">
      <p class="back__message">We have 2 different type of wreath fundraising programs, mail order and direct distribution. You group can choose to do one or both. Wholesale Christmas trees are also available.</p>
      <p class="back__brand">Brandvold<br>Tree Farm</p>
    </div>
    <div class="back__address">
      <div class="stamp-box"></div>
      <ul class="address-lines">
        <li></li><li></li><li></li><li></li><li></li><li></li>
      </ul>
    </div>
  </section>

</body>
</html>
```